Letterhead, business cards, envelopes
Thornwell Holdings Property Management
Creative Brief
Professional
Dean Pultorak
Real Estate Asset Manager
27816 Brisbane Ave., Los Alamitos Ca 90720
dean@thpropertymgmt.example
www.thpropertymgmt.example
designers choice

```html
<!DOCTYPE html>
<html lang="en">
<head>
<meta charset="utf-8">
<title>Thornwell Holdings Property Management – Stationery</title>
<link rel="stylesheet" href="https://fonts.googleapis.com/css2?family=Cinzel:wght@600&family=Open+Sans:wght@400;600&display=swap">
<style>
:root{
  --bg:#ecebe7;
  --paper:#ffffff;
  --green:#1f6b3a;
  --green-dark:#154d29;
  --ink:#3b3b3b;
  --muted:#777;
  --rule:#c9c9c9;
  --field:#eeeeee;
  --black:#141414;
  --faint:#f1f1f1;
}
*{box-sizing:border-box;margin:0;padding:0}
html,body{width:1200px;height:763px;overflow:hidden}
body{background:var(--bg);position:relative;font-family:"Open Sans",Arial,sans-serif;color:var(--ink)}
.piece{position:absolute;background:var(--paper);box-shadow:0 2px 6px rgba(0,0,0,.18);overflow:hidden}

/* brand lockup */
.brand{display:flex;align-items:flex-start;gap:6px}
.brand-square{background:var(--green);flex:none}
.brand-name{font-family:"Cinzel",Georgia,serif;font-weight:600;color:var(--ink);line-height:1.1;text-transform:uppercase;white-space:nowrap}
.brand-rule{height:4px;background:var(--green);margin-top:3px}

/* business cards */
.card{width:228px;height:125px;border-radius:8px}
.card .brand{position:absolute}
.card .brand-square{width:16px;height:16px}
.card .brand-name{font-size:8.5px}
.card-person{position:absolute;font-size:6px;line-height:1.45;color:var(--ink);white-space:nowrap}
.card-person .name{font-weight:600;font-size:6.5px;text-transform:uppercase}
.card-compact .brand-square{width:13px;height:13px}
.card-compact .brand-name{font-size:7px}
.card-compact .brand-rule{height:3px;margin-top:2px}
.card-back{display:flex;flex-direction:column;align-items:center;justify-content:center;gap:8px}
.card-back .brand-square{width:40px;height:40px}
.card-back .web{font-size:6px;letter-spacing:.6px;text-transform:uppercase}
.back-white{background:linear-gradient(#ffffff,#ececec)}
.back-green{background:var(--green)}
.back-green .brand-square{background:#ffffff}
.back-green .web{color:#e5efe8}
.back-black{background:var(--black)}
.back-black .web{color:#cfcfcf}
.faint-square{position:absolute;background:var(--faint)}

/* envelope */
.envelope{left:29px;top:475px;width:566px;height:245px}
.envelope .edge{position:absolute;left:0;top:0;width:8px;height:100%;background:var(--green)}
.envelope .brand{position:absolute;left:24px;top:16px}
.envelope .brand-square{width:26px;height:26px}
.envelope .brand-name{font-size:13px}
.envelope .return{position:absolute;left:24px;bottom:16px;font-size:7px;line-height:1.5;text-transform:uppercase}

/* letterhead / fax */
.letterhead{left:629px;top:19px;width:547px;height:706px}
.letterhead .brand{position:absolute;left:24px;top:20px}
.letterhead .brand-square{width:26px;height:26px}
.letterhead .brand-name{font-size:13px}
.fax-table{position:absolute;left:24px;top:154px;width:475px;border-collapse:separate;border-spacing:0 4px;background:var(--field);padding:4px 6px;font-size:8px}
.fax-table td{padding:3px 4px}
.fax-table .label{width:36px;color:var(--ink)}
.fax-table .field{background:var(--paper);width:190px;height:15px}
.fax-table .gap{width:12px}
.fax-checks{position:absolute;left:24px;top:323px;display:flex;gap:38px;font-size:8px}
.fax-checks span{display:flex;align-items:center;gap:5px}
.fax-checks i{display:inline-block;width:8px;height:8px;border:1px solid var(--muted)}
.letterhead .faint-square{right:36px;bottom:70px;width:150px;height:150px}
.foot-rule{position:absolute;left:24px;right:24px;bottom:22px;height:2px;background:var(--rule)}
.foot-band{position:absolute;left:24px;right:24px;bottom:10px;height:6px;background:var(--green)}
</style>
</head>
<body>

<!-- row 1 -->
<section class="piece card" style="left:72px;top:29px">
  <div class="brand" style="left:12px;top:12px">
    <div class="brand-square"></div>
    <div><div class="brand-name">Thornwell Holdings<br>Property Management</div><div class="brand-rule"></div></div>
  </div>
  <div class="card-person" style="left:92px;top:52px">
    <div class="name">Dean Pultorak</div>
    <div>Real Estate Asset Manager</div>
    <div>T: 562.555.0142</div>
    <div>F: 562.555.0143</div>
    <div>27816 Brisbane Ave., Los Alamitos Ca 90720</div>
    <div>dean@thpropertymgmt.example</div>
  </div>
</section>
<section class="piece card card-back back-white" style="left:317px;top:29px">
  <div class="brand-square"></div>
</section>

<!-- row 2 -->
<section class="piece card" style="left:72px;top:168px">
  <div class="brand" style="left:12px;top:12px">
    <div class="brand-square"></div>
    <div><div class="brand-name">Thornwell Holdings<br>Property Management</div><div class="brand-rule"></div></div>
  </div>
  <div class="card-person" style="left:14px;top:60px">
    <div class="name">Dean Pultorak</div>
    <div>Real Estate Asset Manager</div>
  </div>
  <div class="card-person" style="left:112px;top:60px">
    <div>T: 562.555.0142</div>
    <div>C: 562.555.0144</div>
    <div>27816 Brisbane Ave.</div>
    <div>Los Alamitos Ca 90720</div>
    <div>dean@thpropertymgmt.example</div>
  </div>
</section>
<section class="piece card card-back back-green" style="left:317px;top:168px">
  <div class="brand-square"></div>
  <div class="web">www.thpropertymgmt.example</div>
</section>

<!-- row 3 -->
<section class="piece card card-compact" style="left:72px;top:307px">
  <div class="brand" style="left:12px;top:44px">
    <div class="brand-square"></div>
    <div><div class="brand-name">Thornwell Holdings<br>Property Management</div><div class="brand-rule"></div></div>
  </div>
  <div class="card-person" style="left:138px;top:14px">
    <div class="name">Dean Pultorak</div>
    <div>Real Estate Asset Manager</div>
  </div>
  <div class="card-person" style="left:138px;top:44px">
    <div>27816 Brisbane Ave.</div>
    <div>Los Alamitos Ca 90720</div>
  </div>
  <div class="card-person" style="left:14px;top:90px">
    <div>Residential Commercial Management</div>
    <div>dean@thpropertymgmt.example</div>
  </div>
</section>
<section class="piece card card-back back-black" style="left:317px;top:307px">
  <div class="brand-square"></div>
  <div class="web">www.thpropertymgmt.example</div>
</section>

<!-- envelope -->
<section class="piece envelope">
  <div class="edge"></div>
  <div class="brand">
    <div class="brand-square"></div>
    <div><div class="brand-name">Thornwell Holdings<br>Property Management</div><div class="brand-rule"></div></div>
  </div>
  <div class="faint-square" style="right:40px;top:16px;width:150px;height:150px"></div>
  <div class="return">27816 Brisbane Ave.<br>Los Alamitos Ca 90720</div>
</section>

<!-- fax letterhead -->
<section class="piece letterhead">
  <div class="brand">
    <div class="brand-square"></div>
    <div><div class="brand-name">Thornwell Holdings<br>Property Management</div><div class="brand-rule"></div></div>
  </div>
  <table class="fax-table">
    <tr><td class="label">To:</td><td class="field"></td><td class="gap"></td><td class="label">From:</td><td class="field"></td></tr>
    <tr><td class="label">Fax:</td><td class="field"></td><td class="gap"></td><td class="label">Pages:</td><td class="field"></td></tr>
    <tr><td class="label">Phone:</td><td class="field"></td><td class="gap"></td><td class="label">Date:</td><td class="field"></td></tr>
    <tr><td class="label">Re:</td><td class="field"></td><td class="gap"></td><td class="label">CC:</td><td class="field"></td></tr>
  </table>
  <div class="fax-checks">
    <span><i></i>Urgent</span>
    <span><i></i>For Review</span>
    <span><i></i>Please Comment</span>
    <span><i></i>Please Reply</span>
    <span><i></i>Please Recycle</span>
  </div>
  <div class="faint-square"></div>
  <div class="foot-rule"></div>
  <div class="foot-band"></div>
</section>

</body>
</html>
```